Robotic Physical Therapy office needs a Grand Opening Flyer

We need a Grand Opening flyer design for a robotic physical therapy office named Stellar Motion Therapy. We would like it to have a clean, classy, upscale feeling that gives potential clients a V.I.P. feeling. We would like to use the colors black, gray, and yellow (logo will be uploaded).

Event: Thursday, June 1st, 2023 from 12pm-6pm
location: 58274 Harlow Ave, Bloomfield Hills, MI 48319

Industry/Entity Type

Physical therapy

Font styles to use
Script

Colors

Designer to choose colors to be used in the design.

Requirements
Nice to have
• More of a vip feel for the invite

```html
<!DOCTYPE html>
<html lang="en">
<head>
<meta charset="utf-8">
<title>Stellar Motion Therapy – Grand Opening</title>
<link rel="stylesheet" href="https://fonts.googleapis.com/css2?family=Montserrat:wght@400;500;600;700&family=Oswald:wght@300;400;600&display=swap">
<style>
  :root {
    --backdrop: #2b2b2b;
    --black: #0d0d0d;
    --white: #ffffff;
    --yellow: #f9dc2f;
    --ink: #1f1f24;
    --silver-light: #ffffff;
    --silver-dark: #a9a9a9;
    --circuit: #e4e4e4;
    --photo-top: #e7ebee;
    --photo-bottom: #9aa6b0;
  }
  * { margin: 0; padding: 0; box-sizing: border-box; }
  html, body {
    width: 1200px; height: 1177px; overflow: hidden;
    background: var(--backdrop);
  }
  .flyer {
    position: absolute; left: 256px; top: 140px;
    width: 709px; height: 917px;
    background: var(--white);
    overflow: hidden;
    font-family: "Montserrat", sans-serif;
  }
  .circuit-pattern {
    position: absolute; top: 0; width: 170px; height: 170px;
    background: radial-gradient(circle at top, var(--circuit), transparent 70%);
  }
  .circuit-pattern.left { left: 0; background: radial-gradient(circle at 0 0, var(--circuit), transparent 70%); }
  .circuit-pattern.right { right: 0; background: radial-gradient(circle at 100% 0, var(--circuit), transparent 70%); }

  .brand {
    position: absolute; top: 26px; left: 0; right: 0;
    display: flex; justify-content: center; align-items: center; gap: 14px;
  }
  .brand-mark {
    width: 70px; height: 70px; border-radius: 50%;
    background: var(--ink);
  }
  .brand-name {
    font-weight: 700; font-size: 30px; line-height: 1.05;
    color: var(--ink); text-transform: uppercase;
  }

  .title-band {
    position: absolute; left: 0; top: 174px; width: 100%; height: 106px;
    background: var(--black);
  }
  .title-box {
    position: absolute; left: 78px; top: 143px; width: 548px; height: 79px;
    background: var(--black);
    border: 2px solid var(--yellow);
    display: flex; align-items: center; justify-content: center;
  }
  .title {
    font-weight: 700; font-size: 55px; letter-spacing: 1px;
    background: linear-gradient(180deg, var(--silver-light) 30%, var(--silver-dark));
    -webkit-background-clip: text; background-clip: text; color: transparent;
  }
  .subtitle {
    position: absolute; left: 0; right: 0; top: 236px;
    text-align: center; font-size: 25px; font-weight: 400;
    letter-spacing: 1.5px; color: var(--white);
  }
  .subtitle strong { color: var(--yellow); font-weight: 700; }

  .photo {
    position: absolute; left: 0; top: 280px; width: 100%; height: 375px;
    background: linear-gradient(180deg, var(--photo-top), var(--photo-bottom));
  }

  .details {
    position: absolute; left: 0; top: 655px; width: 100%; height: 210px;
    background: var(--black);
  }
  .date-panel { position: absolute; left: 0; top: 0; }

  .pin-tile {
    position: absolute; left: 0; top: 69px; width: 65px; height: 84px;
    background: var(--yellow);
    display: flex; align-items: center; justify-content: center;
  }
  .address {
    position: absolute; left: 83px; top: 58px;
    color: var(--white); font-size: 26px; font-weight: 400;
    line-height: 33px; letter-spacing: 0.5px; text-transform: uppercase;
  }

  .date-tag {
    position: absolute; background: var(--white); color: var(--black);
    font-family: "Montserrat", sans-serif; font-size: 17px; font-weight: 500;
    letter-spacing: 1px; text-align: center; line-height: 25px;
  }
  .weekday { left: 564px; top: 30px; width: 129px; }
  .hours { left: 566px; top: 159px; width: 127px; }
  .day {
    position: absolute; left: 518px; top: 52px;
    font-family: "Oswald", sans-serif; font-weight: 600;
    font-size: 104px; line-height: 100px; color: var(--black);
  }
  .month {
    position: absolute; left: 569px; top: 58px;
    font-family: "Oswald", sans-serif; font-weight: 600;
    font-size: 41px; line-height: 40px; color: var(--black);
  }
  .year {
    position: absolute; left: 566px; top: 94px;
    font-family: "Oswald", sans-serif; font-weight: 300;
    font-size: 57px; line-height: 60px; color: var(--black);
  }

  .contact {
    position: absolute; left: 0; bottom: 0; width: 100%; height: 52px;
    display: flex; align-items: center; justify-content: center;
    font-size: 18px; letter-spacing: 1px; color: var(--black);
  }
  .contact strong { font-weight: 700; margin-left: 8px; }
</style>
</head>
<body>
  <main class="flyer">
    <div class="circuit-pattern left" role="img" aria-label="Faint circuit board line pattern"></div>
    <div class="circuit-pattern right" role="img" aria-label="Faint circuit board line pattern"></div>

    <header class="brand">
      <span class="brand-mark"></span>
      <span class="brand-name">Stellar Motion<br>Therapy</span>
    </header>

    <div class="title-band"></div>
    <div class="title-box"><h1 class="title">GRAND OPENING</h1></div>
    <p class="subtitle"><strong>ROBOTIC</strong> PHYSICAL THERAPY OFFICE</p>

    <div class="photo" role="img" aria-label="Photo of a patient walking on a treadmill in a robotic leg exoskeleton while a doctor and a nurse watch in a bright therapy room"></div>

    <section class="details">
      <svg class="date-panel" width="709" height="210" viewBox="0 0 709 210" aria-hidden="true">
        <polygon points="503,0 709,0 709,210 432,210" fill="#f9dc2f"/>
      </svg>

      <div class="pin-tile">
        <svg width="26" height="36" viewBox="0 0 26 36" aria-hidden="true">
          <path d="M13 1C6.4 1 1 6.2 1 12.7 1 21.5 13 35 13 35s12-13.5 12-22.3C25 6.2 19.6 1 13 1z" fill="#0d0d0d"/>
          <circle cx="13" cy="12.5" r="4.6" fill="#f9dc2f"/>
        </svg>
      </div>
      <address class="address" style="font-style:normal">
        58274 Harlow Ave,<br>Bloomfield Hills,<br>MI 48319
      </address>

      <div class="date-tag weekday">THURSDAY</div>
      <div class="day">1</div>
      <div class="month">JUNE</div>
      <div class="year">2023</div>
      <div class="date-tag hours">12AM - 6PM</div>
    </section>

    <footer class="contact">FOR MORE INFORMATION PLEASE CONTACT <strong>555 014 2738</strong></footer>
  </main>
</body>
</html>
```